Bookkeeping business needs a digital and print flyer

We need a flyer to promote our virtual bookkeeping services to small and mid-sized businesses in the United States. We want the content and design of the flyer to be consistent with our website: www.brightledgerbookkeeping.example. We would like both a print version and a digital version of the flyer.

```html
<!DOCTYPE html>
<html lang="en">
<head>
<meta charset="utf-8">
<title>Bright Ledger Bookkeeping – Flyer</title>
<link rel="stylesheet" href="https://fonts.googleapis.com/css2?family=Poppins:ital,wght@0,300;0,400;0,600;0,700;0,800;1,600;1,700&display=swap">
<style>
  :root{
    --navy:#0f1440;
    --navy-soft:#2a2d55;
    --yellow:#f2c114;
    --white:#ffffff;
    --paper:#f1f1f2;
    --ink:#1a1a2a;
    --stage:#8fa9a8;
  }
  *{margin:0;padding:0;box-sizing:border-box}
  html,body{width:1200px;height:1117px;overflow:hidden}
  body{background:var(--stage);font-family:'Poppins',sans-serif;color:var(--ink);position:relative}
  .flyer{position:absolute;left:230px;top:33px;width:1030px;height:1460px;transform:scale(0.719);transform-origin:0 0;background:var(--paper);overflow:hidden}
  .flyer-shapes{position:absolute;inset:0}
  .brand{position:absolute;left:0;right:0;top:62px;text-align:center;color:var(--white);font-weight:300;letter-spacing:4px;line-height:1.05}
  .brand-name{font-size:58px;display:block}
  .brand-sub{font-size:30px;display:block;letter-spacing:3px}
  .brand-dot{position:absolute;right:120px;top:12px;width:90px;height:90px;border:3px solid var(--white);border-radius:50%}
  .headline{position:absolute;left:0;right:0;top:205px;text-align:center;font-weight:700;font-size:46px;line-height:50px;color:var(--white)}
  .headline .accent{color:var(--yellow)}
  .tagline{position:absolute;left:0;right:0;top:312px;text-align:center;font-weight:600;font-size:24px;color:var(--white)}
  .benefits{position:absolute;left:112px;top:446px;width:400px}
  .benefits h2{font-size:28px;font-weight:700;line-height:32px;color:var(--navy)}
  .benefits .rule{width:222px;height:3px;background:var(--yellow);margin:12px 0 18px}
  .benefits ul{list-style:none}
  .benefits li{position:relative;padding-left:30px;font-size:19px;line-height:21px;margin-bottom:12px}
  .benefits li svg{position:absolute;left:0;top:3px}
  .benefits em{display:block;font-weight:700}
  .photo{position:absolute;left:510px;top:390px;width:504px;height:504px;border-radius:50%;background:var(--white);padding:14px}
  .photo-frame{width:100%;height:100%;border-radius:50%;background:var(--yellow);padding:15px}
  .photo-fill{width:100%;height:100%;border-radius:50%;background:radial-gradient(circle at 40% 35%,#b8c3dd,#7f8fb8 45%,#d9d6d0 80%)}
  .services{position:absolute;left:110px;top:928px;width:810px;height:357px;background:var(--white);border:3px solid var(--yellow);border-radius:26px}
  .services h3{position:absolute;left:34px;top:28px;width:740px;height:60px;background:var(--navy);border-radius:8px;color:var(--white);font-size:30px;font-weight:600;text-align:center;line-height:60px}
  .services h3 span{color:var(--yellow)}
  .services ul{position:absolute;top:108px;list-style:none;font-size:17.5px;line-height:20px}
  .services .col-left{left:40px;width:400px}
  .services .col-right{left:458px;width:335px}
  .services li{position:relative;padding-left:18px;margin-bottom:12px}
  .services li::before{content:"";position:absolute;left:0;top:8px;width:5px;height:5px;border-radius:50%;background:var(--navy)}
  .services li.plain::before{display:none}
  .cta{position:absolute;left:0;right:0;top:1308px;text-align:center;font-size:30px;font-weight:800;color:var(--navy)}
  .contact{position:absolute;left:0;right:0;top:1365px;height:95px;display:flex;justify-content:center;align-items:center;gap:22px;color:var(--white);font-size:17px;font-weight:700;white-space:nowrap}
  .contact span{display:flex;align-items:center;gap:8px;flex:none}
  .contact svg{flex:none}
</style>
</head>
<body>
<main class="flyer">
  <svg class="flyer-shapes" width="1030" height="1460" viewBox="0 0 1030 1460">
    <defs>
      <linearGradient id="header-tone" x1="0" y1="0" x2="1" y2="1">
        <stop offset="0" stop-color="#2b2e58"/>
        <stop offset="1" stop-color="#22264c"/>
      </linearGradient>
    </defs>
    <polygon points="0,0 1030,0 1030,455 0,365" fill="url(#header-tone)" role="img" aria-label="Laptop keyboard on a desk beside a plant, in dark navy tones"/>
    <polygon points="0,385 275,405 0,430" fill="var(--yellow)"/>
    <polygon points="0,1190 1030,1110 1030,1365 0,1365" fill="var(--yellow)"/>
    <rect x="0" y="1365" width="1030" height="95" fill="var(--navy)"/>
  </svg>

  <div class="brand">
    <span class="brand-name">BRIGHT LEDGER</span>
    <span class="brand-sub">BOOKKEEPING</span>
    <i class="brand-dot"></i>
  </div>

  <h1 class="headline">VIRTUAL BOOKKEEPING FOR SMALL<br><span class="accent">AND MID-SIZED BUSINESSES</span></h1>
  <p class="tagline">Build Your Business by Focusing on What You Love</p>

  <section class="benefits">
    <h2>What you get with<br>Bright Ledger Bookkeeping</h2>
    <div class="rule"></div>
    <ul>
      <li><svg width="16" height="16" viewBox="0 0 16 16"><circle cx="8" cy="8" r="8" fill="#f2c114"/><path d="M4.5 8.2l2.3 2.2 4.7-4.8" stroke="#fff" stroke-width="1.8" fill="none"/></svg>Worry no more about finding time and energy to tackle bookkeeping <em>– Hakuna Matata!</em></li>
      <li><svg width="16" height="16" viewBox="0 0 16 16"><circle cx="8" cy="8" r="8" fill="#f2c114"/><path d="M4.5 8.2l2.3 2.2 4.7-4.8" stroke="#fff" stroke-width="1.8" fill="none"/></svg>Keep more of your hard-earned money by maximizing tax deductions <em>– Ka-Ching!</em></li>
      <li><svg width="16" height="16" viewBox="0 0 16 16"><circle cx="8" cy="8" r="8" fill="#f2c114"/><path d="M4.5 8.2l2.3 2.2 4.7-4.8" stroke="#fff" stroke-width="1.8" fill="none"/></svg>Understand those confusing financial reports to take your business to the next level <em>– Booyah!</em></li>
      <li><svg width="16" height="16" viewBox="0 0 16 16"><circle cx="8" cy="8" r="8" fill="#f2c114"/><path d="M4.5 8.2l2.3 2.2 4.7-4.8" stroke="#fff" stroke-width="1.8" fill="none"/></svg>Celebrate each month’s wins during monthly consultations <em>–Hooray!</em></li>
      <li><svg width="16" height="16" viewBox="0 0 16 16"><circle cx="8" cy="8" r="8" fill="#f2c114"/><path d="M4.5 8.2l2.3 2.2 4.7-4.8" stroke="#fff" stroke-width="1.8" fill="none"/></svg>Stress-free tax time <em>– Oh Yeah!</em></li>
    </ul>
  </section>

  <div class="photo">
    <div class="photo-frame">
      <div class="photo-fill" role="img" aria-label="Stressed business owner at a desk covered in papers, receipts and a calculator"></div>
    </div>
  </div>

  <section class="services">
    <h3>Bookkeeping Tailored to <span>YOUR Business Needs</span></h3>
    <ul class="col-left">
      <li>Catch-up and clean-up services</li>
      <li>Transaction importation and categorization</li>
      <li>Monthly reconciliation of all accounts, including assets and loans.</li>
      <li>Monthly financial reports (Balance Sheet, Income Statement, Cash Flow)</li>
      <li>Monthly video conference</li>
    </ul>
    <ul class="col-right">
      <li>Annual tax-prep package sent to your preparer</li>
      <li>A/R &amp; A/P</li>
      <li>Payroll coordination</li>
      <li class="plain">1099s</li>
      <li>Bill pay and receipt management</li>
      <li>Budgeting</li>
    </ul>
  </section>

  <p class="cta">TAKE BOOKKEEPING OFF YOUR 'TO DO LIST' FOR GOOD!</p>

  <footer class="contact">
    <span><svg width="20" height="20" viewBox="0 0 20 20"><circle cx="10" cy="10" r="10" fill="#f2c114"/><path d="M7 5.5l1.6 2.4-1 1.1c.6 1.3 1.6 2.3 2.9 2.9l1.1-1 2.4 1.6-.8 1.8c-3.6-.3-7.5-4.2-7.8-7.8z" fill="#0f1440"/></svg>555-014-2290</span>
    <span><svg width="20" height="20" viewBox="0 0 20 20"><circle cx="10" cy="10" r="10" fill="#f2c114"/><rect x="5.5" y="7" width="9" height="6.5" fill="none" stroke="#0f1440" stroke-width="1.3"/><path d="M5.5 7l4.5 3.6L14.5 7" fill="none" stroke="#0f1440" stroke-width="1.3"/></svg>mara@brightledgerbookkeeping.example</span>
    <span><svg width="20" height="20" viewBox="0 0 20 20"><circle cx="10" cy="10" r="10" fill="#f2c114"/><circle cx="10" cy="10" r="5" fill="none" stroke="#0f1440" stroke-width="1.3"/><path d="M5 10h10M10 5c-2 2.8-2 7.2 0 10M10 5c2 2.8 2 7.2 0 10" fill="none" stroke="#0f1440" stroke-width="1.1"/></svg>brightledgerbookkeeping.example</span>
  </footer>
</main>
</body>
</html>
```